Sunscreen Package Design Modern SPF 50

Update current package design to a more modern design target women 16-40 Do not make it playful. Sol Mesa is home to movie stars and high income business people PalmSprings is one of the most desired vacation areas in the world. The sun shines 350 days a year. World class Tennis and Golf tournaments are held every year with the worlds top players attending these tournaments

Target Market(s)

Women

Industry/Entity Type

Skin Protection

Font styles to use
Sans Serif

Requirements
Must have
• The words Sol Mesa and VELORIMA

```html
<!DOCTYPE html>
<html lang="en">
<head>
<meta charset="UTF-8">
<title>Sol Mesa VELORIMA – Sun Care Tube</title>
<link href="https://fonts.googleapis.com/css2?family=Montserrat:wght@400;500&family=Roboto+Condensed:wght@400;700&display=swap" rel="stylesheet">
<style>
  :root {
    --bg: #ffffff;
    --gold: #d9a23a;
    --cap: #c9a85a;
    --cap-light: #dcc17a;
    --teal-light: #e9f5f8;
    --teal-mid: #a9d6df;
    --teal: #4fa2b2;
    --teal-deep: #2f8396;
    --ink: #14181a;
    --aqua-text: #b9f1f4;
    --white: #ffffff;
  }
  html, body { margin: 0; padding: 0; overflow: hidden; background: var(--bg); }
  .stage { position: relative; width: 1200px; height: 1200px; background: var(--bg); overflow: hidden; }

  .tube-shell { position: absolute; left: 0; top: 0; width: 1200px; height: 1200px; filter: drop-shadow(0 0 1.5px rgba(0,0,0,0.14)); }
  .tube-body {
    position: absolute; left: 424px; top: 126px; width: 354px; height: 843px;
    clip-path: polygon(0 0, 100% 0, 80% 100%, 20% 100%);
    background: linear-gradient(180deg, #ffffff 0%, #ffffff 22%, var(--teal-light) 40%, var(--teal-mid) 58%, var(--teal) 82%, var(--teal-deep) 100%);
  }
  .tube-crimp { position: absolute; left: 0; top: 0; width: 100%; height: 38px;
    background: repeating-linear-gradient(90deg, #f2f2f2 0 2px, #ffffff 2px 4px); }
  .scene-art {
    position: absolute; left: 60px; top: 440px; width: 234px; height: 403px;
    background: linear-gradient(180deg, rgba(79,162,178,0) 0%, rgba(63,145,162,0.45) 45%, rgba(40,120,138,0.6) 100%);
  }

  .brand-dot { position: absolute; left: 550px; top: 218px; width: 100px; height: 100px; border-radius: 50%; background: var(--gold); }
  .brand-name {
    position: absolute; left: 0; width: 1200px; text-align: center; margin: 0;
    font-family: "Roboto Condensed", sans-serif; font-weight: 400; color: var(--gold);
    font-size: 82px; line-height: 1; letter-spacing: 4px;
  }
  .brand-line-1 { top: 362px; }
  .brand-line-2 { top: 436px; }
  .brand-sub {
    position: absolute; left: 0; top: 519px; width: 1200px; text-align: center;
    font-family: "Montserrat", sans-serif; font-weight: 500; font-size: 20px; letter-spacing: 6px; color: var(--gold);
  }

  .feature { position: absolute; display: flex; align-items: center; gap: 12px; }
  .feature svg { flex: none; }
  .feature-text {
    font-family: "Roboto Condensed", sans-serif; font-weight: 700; font-size: 19px; line-height: 21px;
    color: var(--ink); text-transform: uppercase; letter-spacing: -0.2px;
  }
  .feature-aloe { left: 491px; top: 584px; }
  .feature-cucumber { left: 498px; top: 662px; }
  .feature-tan { left: 503px; top: 734px; }
  .divider { position: absolute; height: 1.5px; background: var(--ink); }
  .divider-1 { left: 496px; top: 645px; width: 210px; }
  .divider-2 { left: 501px; top: 717px; width: 200px; }

  .claim, .ingredients {
    position: absolute; left: 0; width: 1200px; text-align: center; margin: 0;
    font-family: "Roboto Condensed", sans-serif; font-weight: 400; color: var(--aqua-text); text-transform: uppercase;
  }
  .claim { top: 803px; font-size: 14px; line-height: 17px; }
  .ingredients { top: 869px; font-size: 13px; line-height: 16px; }
  .volume {
    position: absolute; left: 0; top: 940px; width: 1200px; text-align: center;
    font-family: "Montserrat", sans-serif; font-size: 11px; color: var(--white);
  }

  .tube-cap {
    position: absolute; left: 497px; top: 962px; width: 208px; height: 110px;
    border-radius: 0 0 6px 6px;
    background: linear-gradient(90deg, var(--cap) 0%, var(--cap-light) 50%, var(--cap) 100%);
  }
  .cap-band { position: absolute; left: 0; top: 86px; width: 100%; height: 2px; background: rgba(0,0,0,0.08); }
</style>
</head>
<body>
<main class="stage">
  <div class="tube-shell">
    <div class="tube-body">
      <div class="tube-crimp"></div>
      <div class="scene-art" role="img" aria-label="Line illustration of a desert mid-century house, pool, palm trees, mountains and vintage car in teal tones"></div>
    </div>
  </div>

  <div class="brand-dot"></div>
  <h1 class="brand-name brand-line-1">SOL</h1>
  <h1 class="brand-name brand-line-2">MESA</h1>
  <div class="brand-sub">VELORIMA</div>

  <div class="feature feature-aloe">
    <svg width="40" height="46" viewBox="0 0 42 48" fill="none" stroke="#14181a" stroke-width="1.6" stroke-linejoin="round">
      <path d="M21 46 C16 32 17 16 21 2 C25 16 26 32 21 46 Z"/>
      <path d="M19 46 C10 38 5 26 4 14 C12 24 17 34 19 46 Z"/>
      <path d="M23 46 C32 38 37 26 38 14 C30 24 25 34 23 46 Z"/>
    </svg>
    <div class="feature-text">Intense Soothing<br>Aloe &amp; Jojoba</div>
  </div>
  <div class="divider divider-1"></div>

  <div class="feature feature-cucumber">
    <svg width="34" height="34" viewBox="0 0 36 36" fill="none" stroke="#14181a" stroke-width="1.6">
      <circle cx="18" cy="18" r="16"/>
      <circle cx="18" cy="18" r="11"/>
      <circle cx="18" cy="18" r="3"/>
    </svg>
    <div class="feature-text">Cooling Cucumber<br>Hydration</div>
  </div>
  <div class="divider divider-2"></div>

  <div class="feature feature-tan">
    <svg width="34" height="34" viewBox="0 0 36 36" fill="none" stroke="#14181a" stroke-width="1.6" stroke-linecap="round">
      <circle cx="18" cy="18" r="8"/>
      <path d="M18 2v5M18 29v5M2 18h5M29 18h5M6.7 6.7l3.5 3.5M25.8 25.8l3.5 3.5M6.7 29.3l3.5-3.5M25.8 10.2l3.5-3.5"/>
    </svg>
    <div class="feature-text">Tan Enhancing<br>Formula</div>
  </div>

  <p class="claim">Hydrate your skin with<br>these essential<br>ingredients</p>
  <p class="ingredients">Hyaluronate acid cucumber<br>aloe jojoba sunflower</p>
  <div class="volume">3 FL OZ / 88 mL</div>

  <div class="tube-cap"><div class="cap-band"></div></div>
</main>
</body>
</html>
```